Fabric Softener

We need fabric softener. Bottle picture attached for reference. Color of bottle can be proposed as well. Normally bottle is pink and blue color

Logo is also attached that shall be used.
Updates

Need extra days to review

Low designer entries

Target Market(s)

Niche

Font styles to use
Sans Serif

Requirements
Must have
• Fabric, Brightness, Nature
Nice to have
• Good colors
Should not have
• Adults

```html
<!DOCTYPE html>
<html lang="en">
<head>
<meta charset="utf-8">
<title>Velora Fabric Softener – Starlit Lavender Label</title>
<link rel="stylesheet" href="https://fonts.googleapis.com/css2?family=Roboto:wght@400;500;700&family=Roboto+Condensed:wght@400;700&display=swap">
<style>
  :root {
    --page: #f4f1f8;
    --label-deep: #2c2a6b;
    --label-violet: #6a4fb3;
    --label-rose: #b5649e;
    --label-lilac: #8a6ad0;
    --ribbon: rgba(200, 170, 240, 0.75);
    --white: #ffffff;
    --lavender-field: #7d5bc4;
    --lavender-green: #6d8f4a;
  }
  * { margin: 0; padding: 0; box-sizing: border-box; }
  html, body { width: 1000px; height: 1200px; overflow: hidden; background: var(--page); }
  .canvas { position: relative; width: 1000px; height: 1200px; font-family: "Roboto", Arial, sans-serif; }
  .label-art { position: absolute; inset: 0; }
  .galaxy-start { stop-color: var(--label-lilac); }
  .galaxy-deep { stop-color: var(--label-deep); }
  .galaxy-rose { stop-color: var(--label-rose); }
  .galaxy-end { stop-color: var(--label-violet); }
  .field-top { stop-color: var(--lavender-field); stop-opacity: 0; }
  .field-mid { stop-color: var(--lavender-field); }
  .field-base { stop-color: var(--lavender-green); }
  .variant-ribbon { fill: var(--ribbon); }
  .product-type {
    position: absolute; left: 170px; top: 430px;
    color: var(--white); font-size: 22px; line-height: 1.45; font-weight: 500;
  }
  .brand {
    position: absolute; left: 150px; top: 530px;
    display: flex; align-items: center; gap: 14px;
    color: var(--white); font-size: 104px; font-weight: 700; letter-spacing: -1px; line-height: 1.1;
  }
  .brand-dot { width: 22px; height: 22px; border-radius: 50%; background: var(--white); }
  .variant {
    position: absolute; left: 175px; top: 724px;
    color: var(--white); font-size: 34px; font-weight: 500; letter-spacing: 0.5px;
  }
  .loads-badge {
    position: absolute; left: 748px; top: 598px; width: 112px; height: 112px;
    border: 3px solid var(--white); border-radius: 50%;
    display: flex; flex-direction: column; align-items: center; justify-content: center;
    color: var(--white); font-family: "Roboto Condensed", Arial, sans-serif;
  }
  .loads-badge .count { font-size: 38px; font-weight: 700; line-height: 1; }
  .loads-badge .unit { font-size: 19px; line-height: 1.1; }
  .net-volume {
    position: absolute; left: 0; right: 0; top: 968px; text-align: center;
    color: var(--white); font-family: "Roboto Condensed", Arial, sans-serif; font-size: 26px;
  }
</style>
</head>
<body>
<main class="canvas">
  <svg class="label-art" width="1000" height="1200" viewBox="0 0 1000 1200">
    <defs>
      <linearGradient id="galaxy" x1="0" y1="0" x2="1" y2="1">
        <stop offset="0" class="galaxy-start"/>
        <stop offset="0.35" class="galaxy-deep"/>
        <stop offset="0.6" class="galaxy-rose"/>
        <stop offset="1" class="galaxy-end"/>
      </linearGradient>
      <linearGradient id="flowers" x1="0" y1="0" x2="0" y2="1">
        <stop offset="0" class="field-top"/>
        <stop offset="0.45" class="field-mid"/>
        <stop offset="1" class="field-base"/>
      </linearGradient>
      <clipPath id="label-clip">
        <path d="M120 300 Q120 150 250 130 Q330 120 360 200 L360 470 Q380 560 480 560 L860 560 Q900 560 900 600 L900 1000 Q900 1070 830 1070 L190 1070 Q120 1070 120 1000 Z"/>
      </clipPath>
    </defs>
    <path class="label-body" role="img" aria-label="Starry purple night sky with lilac blossoms at the top"
      d="M120 300 Q120 150 250 130 Q330 120 360 200 L360 470 Q380 560 480 560 L860 560 Q900 560 900 600 L900 1000 Q900 1070 830 1070 L190 1070 Q120 1070 120 1000 Z"
      fill="url(#galaxy)"/>
    <g clip-path="url(#label-clip)">
      <rect class="lavender-bouquet" role="img" aria-label="Lavender sprigs and violet flowers" x="120" y="760" width="780" height="310" fill="url(#flowers)"/>
      <path class="variant-ribbon" d="M120 712 Q400 690 720 700 L720 780 Q400 772 120 790 Z"/>
    </g>
  </svg>

  <p class="product-type">Fabric<br>Softener</p>
  <div class="brand"><span class="brand-dot"></span>Velora</div>
  <p class="variant">Starlit Lavender</p>
  <div class="loads-badge"><span class="count">120</span><span class="unit">LOADS</span></div>
  <p class="net-volume">3.06 L (3.23 US QT/PTE É-U) 103 FL OZ</p>
</main>
</body>
</html>
```